Real Estate Marketing for home owners

We are needing a logo and post card design with white paper, blue ink, in 4X6 size for mail out to home owners. We are wanting the font to be in Helvetica. We want to draw the reader in as we are "pay all closing cost" and are direct buyers.Wanting the "hand shake" design as a watermark behind the writing. Make sure that we have the "A+ QLC logo" in there.

Target Market(s)

Home Owners and Non Home Owners that own a residential property

Industry/Entity Type

Real Estate

Font styles to use
Other font styles liked:
• Helvetica

Colors
0455a3
ffffff

Requirements
Must have
• A+ QLC Logo, Hand shake watermark, read: Need $$$ Fast? Sell your Property in any condition AS-IS for ALL-CASH. Close in 7 days or Less! (January Bonus Offer: We will pay 100% of your closing costs AND give you a $1000 Move-Out Credit! Call Mila Dorsen NOW for a Free, No Obligation, Friendly Conversation About your Property.
• 555-014-2837 mila@sturdyfundhouse.example
• Sturdy Fund House. (example attached)
Nice to have
• Something that will draw a reader to call us rather than throw it in the trash when they get it.

```html
<!DOCTYPE html>
<html lang="en">
<head>
<meta charset="utf-8">
<title>Sturdy Fund House – Postcard</title>
<link rel="stylesheet" href="https://fonts.googleapis.com/css2?family=Roboto+Condensed:wght@400;700;900&family=Roboto:wght@900&display=swap">
<style>
  :root {
    --brand-blue: #0455a3;
    --ink: #0a0a0a;
    --paper: #ffffff;
    --mist-light: #f7f7f7;
    --mist-mid: #e3e3e3;
    --mist-dark: #cfcfcf;
  }
  * { margin: 0; padding: 0; box-sizing: border-box; }
  html, body { width: 1200px; height: 816px; overflow: hidden; background: var(--paper); }
  .postcard {
    position: relative; width: 1200px; height: 816px; overflow: hidden;
    font-family: "Roboto Condensed", "Helvetica Neue", Arial, sans-serif;
    color: var(--ink);
  }
  .handshake-watermark {
    position: absolute; inset: 0;
    background:
      radial-gradient(ellipse 360px 220px at 560px 470px, var(--mist-dark), transparent 75%),
      radial-gradient(ellipse 520px 300px at 900px 260px, var(--mist-mid), transparent 75%),
      radial-gradient(ellipse 420px 260px at 200px 300px, var(--mist-mid), transparent 75%),
      var(--mist-light);
  }
  .headline {
    position: absolute; top: 82px; left: 0; width: 100%; text-align: center;
    font-weight: 900; font-size: 66px; line-height: 1; color: var(--brand-blue); letter-spacing: -0.5px;
  }
  .pitch {
    position: absolute; top: 156px; left: 0; width: 100%; text-align: center;
    font-weight: 700; font-size: 35px; line-height: 38px;
  }
  .bonus-tag {
    position: absolute; top: 279px; left: 155px; width: 204px; height: 72px;
    background: var(--brand-blue); color: var(--paper);
    font-weight: 700; font-size: 29px; line-height: 36px; text-align: center;
    display: flex; flex-direction: column; justify-content: center;
  }
  .bonus-arrow { position: absolute; top: 279px; left: 367px; }
  .bonus-text {
    position: absolute; top: 270px; left: 400px;
    font-size: 37px; line-height: 48px;
  }
  .bonus-text .credit { color: var(--brand-blue); font-weight: 700; font-size: 42px; }
  .call-line {
    position: absolute; top: 418px; left: 0; width: 100%; text-align: center;
    font-size: 47px; line-height: 50px;
  }
  .call-line .call { color: var(--brand-blue); }
  .call-line .agent { font-weight: 700; }
  .call-sub {
    position: absolute; top: 465px; left: 0; width: 100%; text-align: center;
    font-size: 35px; line-height: 40px;
  }
  .accreditation-badge { position: absolute; top: 537px; left: 130px; }
  .accreditation-link {
    position: absolute; top: 724px; left: 110px; width: 156px; text-align: center;
    font-family: Arial, Helvetica, sans-serif; font-size: 14px; color: var(--brand-blue);
  }
  .phone-icon { position: absolute; top: 573px; left: 335px; }
  .phone-number {
    position: absolute; top: 580px; left: 418px;
    font-family: "Roboto", Arial, sans-serif; font-weight: 900; font-size: 60px; line-height: 62px;
    letter-spacing: 5px;
  }
  .phone-rule { position: absolute; top: 641px; left: 418px; width: 456px; height: 3px; background: var(--ink); }
  .mail-icon { position: absolute; top: 656px; left: 350px; }
  .email {
    position: absolute; top: 646px; left: 422px;
    font-size: 35px; line-height: 42px;
  }
</style>
</head>
<body>
<main class="postcard">
  <div class="handshake-watermark" role="img" aria-label="Faint black and white photo of two people shaking hands, used as a watermark"></div>

  <h1 class="headline">Need $$$ Fast?</h1>
  <p class="pitch">Sell your Property in any condition AS-IS for ALL-CASH.<br>Close in 7 days or Less!</p>

  <div class="bonus-tag"><span>JANUARY</span><span>BONUS OFFER</span></div>
  <svg class="bonus-arrow" width="26" height="72" viewBox="0 0 26 72" aria-hidden="true">
    <polygon points="0,0 26,36 0,72" fill="var(--brand-blue)"/>
  </svg>
  <p class="bonus-text">We will pay 100% of your closing costs<br>AND give you a <span class="credit">$1000</span> Move-Out Credit!</p>

  <p class="call-line"><span class="call">Call</span> <span class="agent">Mila Dorsen NOW</span></p>
  <p class="call-sub">for a Free, No Obligation, Friendly Conversation About your Property.</p>

  <svg class="accreditation-badge" width="116" height="181" viewBox="0 0 116 181" role="img" aria-label="QLC accreditation badge">
    <rect x="1" y="1" width="114" height="179" rx="8" fill="var(--paper)" stroke="var(--brand-blue)" stroke-width="2"/>
    <rect x="7" y="140" width="102" height="34" rx="4" fill="var(--brand-blue)"/>
  </svg>
  <p class="accreditation-link">qlc.example/charity</p>

  <svg class="phone-icon" width="70" height="70" viewBox="0 0 70 70" aria-hidden="true">
    <circle cx="35" cy="35" r="32" fill="none" stroke="var(--brand-blue)" stroke-width="4"/>
    <path d="M24 18c2-2 5-2 6 0l4 7c1 2 0 4-1 5l-3 2c2 5 5 9 9 11l2-3c1-2 3-2 5-1l6 4c2 1 2 4 0 6l-3 3c-3 2-8 1-13-3-6-5-11-11-13-18-1-5 0-9 1-11z" fill="none" stroke="var(--brand-blue)" stroke-width="3" stroke-linejoin="round"/>
  </svg>
  <p class="phone-number">555-014-2837</p>
  <div class="phone-rule"></div>

  <svg class="mail-icon" width="40" height="24" viewBox="0 0 40 24" aria-hidden="true">
    <rect x="0" y="0" width="40" height="24" fill="var(--brand-blue)"/>
    <path d="M1 1l19 13 19-13M1 23l14-11M39 23l-14-11" fill="none" stroke="var(--paper)" stroke-width="2"/>
  </svg>
  <p class="email">mila@sturdyfundhouse.example</p>
</main>
</body>
</html>
```